Business Card - Harlow Birch

Need Business Card design for company named Harlow Birch. Software development focused mainly on Ardel eKallo & oBix Apps. I've attached our logo with both a black and white background. Please add trademark symbol to logo when using.

```html
<!DOCTYPE html>
<html lang="en">
<head>
<meta charset="utf-8">
<title>Harlow Birch — Business Card</title>
<link rel="stylesheet" href="https://fonts.googleapis.com/css2?family=Arimo:wght@700&display=swap">
<style>
  :root {
    --backdrop: #2b2b2b;
    --green-top: #5cff4f;
    --green-bottom: #10f000;
    --dark-top: #4a4a4a;
    --dark-bottom: #000000;
    --ink: #000000;
    --paper: #ffffff;
    --accent-orange: #f07800;
    --accent-green: #3ef03a;
  }
  * { box-sizing: border-box; margin: 0; padding: 0; }
  html, body {
    width: 1200px; height: 792px; overflow: hidden;
    background: var(--backdrop);
    font-family: "Arimo", Arial, sans-serif;
  }
  .canvas {
    position: relative; width: 1200px; height: 792px;
    display: flex; align-items: center; justify-content: center; gap: 120px;
  }
  .card {
    position: relative; width: 420px; height: 250px; overflow: hidden;
  }
  .card--front {
    background: linear-gradient(180deg, var(--green-top), var(--green-bottom));
    border-bottom-left-radius: 26px;
  }
  .card--back {
    background: linear-gradient(180deg, var(--dark-top), var(--dark-bottom));
    border-bottom-right-radius: 26px;
  }
  .side-bar {
    position: absolute; width: 12px; border-radius: 6px;
  }
  .card--front .side-bar { background: var(--ink); }
  .card--back .side-bar { background: var(--accent-green); }
  .side-bar--left { left: 16px; top: 92px; height: 132px; }
  .side-bar--right { right: 16px; top: 40px; height: 132px; }
  .card--back .side-bar--left { top: 104px; }
  .card--back .side-bar--right { top: 40px; }

  .brand {
    position: absolute; left: 0; right: 0; top: 70px;
    display: flex; align-items: center; justify-content: center; gap: 10px;
  }
  .card--back .brand { top: 100px; }
  .brand__square {
    width: 22px; height: 22px; background: var(--accent-orange);
  }
  .brand__name {
    font-size: 22px; font-weight: 700;
  }
  .card--front .brand__name { color: var(--ink); }
  .card--back .brand__name { color: var(--paper); }
  .brand__tm { font-size: 11px; vertical-align: super; }

  .contact-icon {
    position: absolute; width: 22px; height: 22px;
  }
  .contact-icon--pin { left: 96px; top: 170px; }
  .contact-icon--mail { left: 196px; top: 148px; }
  .contact-icon--phone { left: 318px; top: 116px; }

  .detail-lines {
    position: absolute; left: 46px; right: 22px; bottom: 26px;
    display: flex; gap: 6px;
  }
  .detail-line {
    flex: 1; height: 2px; background: var(--ink);
  }
</style>
</head>
<body>
<main class="canvas">
  <section class="card card--front" aria-label="Card front">
    <span class="side-bar side-bar--left"></span>
    <span class="side-bar side-bar--right"></span>
    <div class="brand">
      <span class="brand__square"></span>
      <span class="brand__name">Harlow Birch<span class="brand__tm">™</span></span>
    </div>
    <svg class="contact-icon contact-icon--pin" viewBox="0 0 24 24" aria-label="Address">
      <path d="M12 22 C9 16 7 12 7 9 a5 5 0 0 1 10 0 c0 3 -2 7 -5 13z" fill="var(--accent-orange)"/>
    </svg>
    <svg class="contact-icon contact-icon--mail" viewBox="0 0 24 24" aria-label="Email">
      <text x="12" y="18" text-anchor="middle" font-size="20" font-family="Arimo, Arial, sans-serif" fill="var(--accent-orange)">@</text>
    </svg>
    <svg class="contact-icon contact-icon--phone" viewBox="0 0 24 24" aria-label="Phone">
      <path d="M6 3 L9 3 L10.5 8 L8.5 9.5 C9.5 12 12 14.5 14.5 15.5 L16 13.5 L21 15 L21 18 C21 19.5 19.5 21 18 21 C10 20.5 3.5 14 3 6 C3 4.5 4.5 3 6 3 Z" fill="var(--accent-orange)"/>
    </svg>
    <div class="detail-lines">
      <span class="detail-line"></span>
      <span class="detail-line"></span>
      <span class="detail-line"></span>
    </div>
  </section>

  <section class="card card--back" aria-label="Card back">
    <span class="side-bar side-bar--left"></span>
    <span class="side-bar side-bar--right"></span>
    <div class="brand">
      <span class="brand__square"></span>
      <span class="brand__name">Harlow Birch<span class="brand__tm">™</span></span>
    </div>
  </section>
</main>
</body>
</html>
```